Stationary for Green cleaners and green products
Fresh Leaf Laundry n Goods
Stationary for Green cleaners and green products - Retailers
Creative Brief
Use same font as used in my logo
Harold J Benton
President
4730 Maple Row Fernwood, KY 40123
606-514-7720 or 514-7721
1freshleaflaundry@mailbox-example.com
freshleaflaundry-example.org or.net or .biz
logo also being developed at this site
list of services Dry Cleaning Laundry household items, draperies, leather, wedding gowns, full alterations services green friendly products
Concepts
Business Cards/Letterhead/ Envelopes/Notepads/Tshirt/labels for little big box
Business Card for Womens Clothing Boutique

```html
<!DOCTYPE html>
<html lang="en">
<head>
<meta charset="utf-8">
<title>Fresh Leaf Laundry n Goods – Business Card</title>
<link rel="stylesheet" href="https://fonts.googleapis.com/css2?family=Open+Sans:wght@400;600;700;800&display=swap">
<style>
  :root {
    --green-deep: #2e7d32;
    --green-mid: #3f9b3a;
    --green-light: #8cc63f;
    --paper: #ffffff;
    --stage: #e9ece9;
    --ink: #3a4a3a;
    --ink-soft: #5c6b5c;
  }
  * { box-sizing: border-box; margin: 0; padding: 0; }
  html, body { width: 1200px; height: 1009px; overflow: hidden; }
  body {
    background: var(--stage);
    font-family: "Open Sans", Arial, sans-serif;
    display: flex; flex-direction: column; align-items: center;
    justify-content: space-evenly;
  }
  .card {
    position: relative; width: 760px; height: 434px;
    border-radius: 22px; overflow: hidden;
    box-shadow: 0 6px 18px rgba(0,0,0,.15);
  }
  /* front */
  .card--front { background: var(--paper); }
  .card__swoosh { position: absolute; inset: 0; width: 100%; height: 100%; }
  .brand { position: absolute; display: flex; align-items: center; gap: 14px; white-space: nowrap; }
  .card--front .brand { left: 48px; top: 70px; }
  .brand__dot { width: 46px; height: 46px; border-radius: 50%; background: var(--green-mid); flex: none; }
  .brand__name { font-weight: 700; color: var(--green-mid); font-size: 30px; line-height: 1.05; }
  .brand__name small { display: block; font-size: 18px; text-align: right; margin-top: 2px; }
  .brand__rule { position: absolute; left: 48px; top: 160px; width: 300px; height: 2px; background: var(--green-light); }
  .contact { position: absolute; left: 420px; top: 56px; list-style: none; font-size: 15px; color: var(--ink); line-height: 1.55; }
  .contact li { display: flex; align-items: center; gap: 8px; white-space: nowrap; }
  .contact svg { width: 13px; height: 13px; fill: var(--green-mid); flex: none; }
  .contact .contact__address { padding-left: 21px; }
  .person { position: absolute; right: 44px; bottom: 34px; color: #fff; text-align: right; }
  .person__name { font-size: 22px; font-weight: 700; }
  .person__role { font-size: 15px; }
  /* back */
  .card--back { background: var(--green-mid); color: #fff; text-align: center; }
  .card--back .brand { left: 50%; top: 92px; transform: translateX(-50%); }
  .card--back .brand__dot { background: #fff; }
  .card--back .brand__name { color: #fff; font-size: 34px; text-align: left; }
  .services { position: absolute; left: 0; right: 0; top: 210px; font-size: 16px; line-height: 1.6; }
  .services__main { font-weight: 600; }
</style>
</head>
<body>

  <section class="card card--front">
    <svg class="card__swoosh" viewBox="0 0 760 434" preserveAspectRatio="none" aria-hidden="true">
      <path d="M0 300 C200 250 420 330 760 270 L760 434 L0 434 Z" fill="var(--green-light)"/>
      <path d="M0 325 C220 275 440 360 760 300 L760 434 L0 434 Z" fill="var(--paper)"/>
      <path d="M0 340 C230 295 450 375 760 318 L760 434 L0 434 Z" fill="var(--green-mid)"/>
    </svg>

    <div class="brand">
      <span class="brand__dot"></span>
      <div class="brand__name">Fresh Leaf Laundry<small>n Goods</small></div>
    </div>
    <span class="brand__rule"></span>

    <ul class="contact">
      <li class="contact__address">4730 Maple Row</li>
      <li class="contact__address">Fernwood, KY 40123</li>
      <li><svg viewBox="0 0 24 24"><path d="M6.6 10.8a15 15 0 006.6 6.6l2.2-2.2a1 1 0 011-.25 11.4 11.4 0 003.6.6 1 1 0 011 1V20a1 1 0 01-1 1A17 17 0 013 4a1 1 0 011-1h3.5a1 1 0 011 1c0 1.25.2 2.45.6 3.6a1 1 0 01-.25 1z"/></svg>606-514-7720</li>
      <li><svg viewBox="0 0 24 24"><path d="M6.6 10.8a15 15 0 006.6 6.6l2.2-2.2a1 1 0 011-.25 11.4 11.4 0 003.6.6 1 1 0 011 1V20a1 1 0 01-1 1A17 17 0 013 4a1 1 0 011-1h3.5a1 1 0 011 1c0 1.25.2 2.45.6 3.6a1 1 0 01-.25 1z"/></svg>606-514-7721</li>
      <li><svg viewBox="0 0 24 24"><path d="M2 5h20v14H2z M2 5l10 8 10-8" /></svg>1freshleaflaundry@mailbox-example.com</li>
      <li><svg viewBox="0 0 24 24"><circle cx="12" cy="12" r="10"/></svg>www.freshleaflaundry-example.org</li>
    </ul>

    <div class="person">
      <div class="person__name">Harold J Benton</div>
      <div class="person__role">President</div>
    </div>
  </section>

  <section class="card card--back">
    <div class="brand">
      <span class="brand__dot"></span>
      <div class="brand__name">Fresh Leaf Laundry<small>n Goods</small></div>
    </div>
    <div class="services">
      <p class="services__main">Dry Cleaning</p>
      <p class="services__main">Laundry</p>
      <p>Household Items, Draperies, Leather, Wedding Gowns, Full Alterations Services</p>
      <p>Green Friendly Products</p>
    </div>
  </section>

</body>
</html>
```